Tarn Studio PPT design

We are looking for a fresh and funky PPT design that is both eye-catching and allows room/whitespace for us to get the content across. We are a social media agency based in China and our logo although simple sort of reflects the nature of the company. There are two main tasks for this PPT, one as a business card to show-case our case-studies, but also as a back-drop to our pitch presentations and other client presentations. These presentations are a mix of visuals, text and graphs. The key message we want to get across is that we are professional, creative and fresh. We think that using our four support colours may work but are open to suggestions.
Current website www.tarnasia-example.com
Reason: Hi All,
as we have just guaranteed the payment we extended the deadline to allow for more submissions. Please bear with us.
Thanks,
Tarn Studio Team
Reason: To see more designs, we extend the deadline to March 18, 2014. Thanks.
Target Market(s)
Marketing CMO's, company CEO's, product managers, social media managers
Industry/Entity Type
Business

```html
<!DOCTYPE html>
<html lang="en">
<head>
<meta charset="utf-8">
<title>Tarn Studio – Title Slide</title>
<link rel="stylesheet" href="https://fonts.googleapis.com/css2?family=Arimo:wght@400;700&display=swap">
<style>
  :root {
    --stage: #000000;
    --header-band: #2d303b;
    --slide-body: #f0f0f0;
    --brand-white: #ffffff;
    --title-purple: #8a35a0;
    --subtitle-green: #5fcf3e;
  }
  html, body {
    margin: 0;
    padding: 0;
    width: 1200px;
    height: 1000px;
    overflow: hidden;
    background: var(--stage);
    font-family: "Arimo", Arial, sans-serif;
  }
  .slide {
    position: absolute;
    left: 29px;
    top: 72px;
    width: 1142px;
    height: 856px;
    background: var(--slide-body);
    overflow: hidden;
  }
  .slide-header {
    position: absolute;
    left: 0;
    top: 0;
    width: 100%;
    height: 343px;
    background: var(--header-band);
  }
  .brand-name {
    position: absolute;
    left: 72px;
    top: 68px;
    margin: 0;
    font-size: 30px;
    font-weight: 700;
    line-height: 1;
    color: var(--brand-white);
    white-space: nowrap;
  }
  .slide-title {
    position: absolute;
    left: 83px;
    top: 593px;
    margin: 0;
    font-size: 47px;
    font-weight: 700;
    line-height: 1;
    letter-spacing: -0.5px;
    color: var(--title-purple);
    white-space: nowrap;
  }
  .slide-subtitle {
    position: absolute;
    left: 83px;
    margin: 0;
    font-size: 24px;
    font-weight: 400;
    line-height: 1;
    color: var(--subtitle-green);
    white-space: nowrap;
  }
  .slide-subtitle--first { top: 705px; }
  .slide-subtitle--second { top: 750px; }
</style>
</head>
<body>
  <main class="slide">
    <header class="slide-header">
      <p class="brand-name">Tarn Studio</p>
    </header>
    <h1 class="slide-title">LOREM IPSUM DOLOR SIT AMET</h1>
    <p class="slide-subtitle slide-subtitle--first">Lorem ipsum dolor sit amet</p>
    <p class="slide-subtitle slide-subtitle--second">Lorem ipsum dolor sit amet</p>
  </main>
</body>
</html>
```